Hallo,
ich benötige für ein bereits fertiges Cover noch einige Grafiken um das Buch auf SociaMedia zu bewerben.
Nachdem es sich um einen Erotikroman handelt, geschrieben aus der Sicht eines Mannes, gehe ich davon aus, das das hauptsächlich Männer interessieren wird.
Es handelt sich um folgenden Roman: https://www.buchkiste-online.de/dp/X7QRTZ4K2M
Aufgabenstellung
Die benötigten Grafiken im einzelnen:
* Hochformat: 660 x 1173 Pixel
* Quadratisch: 1080 Pixel
* Querformat: 1173 x 660 Pixel
Die Bilder sollten beinhalten:
* Das Cover
* Der Text 'Jetzt im Handel' und 'Zum Einführungspreis von xx%'
* Die Beschreibung des Buches sollte gut lesbar vorkommen:
Eines Tages kauft der Student Kilian ein neuartiges Online-Computerspiel und weiß zu diesem Zeitpunkt noch nicht, dass sich sein Sex-Leben dadurch drastisch verbessern wird.

```html
<!DOCTYPE html>
<html lang="de">
<head>
<meta charset="utf-8">
<title>Nächte in Veloria – Social-Media-Anzeigen</title>
<link rel="stylesheet" href="https://fonts.googleapis.com/css2?family=EB+Garamond:ital,wght@0,500;0,600;1,500&family=Cinzel:wght@400;600&family=Open+Sans:wght@400;700&display=swap">
<style>
  :root {
    --page-bg: #e6e6e6;
    --panel-dark: #1f2021;
    --panel-mid: #4a4e50;
    --panel-light: #7a8184;
    --text-light: #f4f4f2;
    --text-shadow: rgba(0,0,0,0.75);
    --cover-forest: #9aa5a6;
    --cover-shade: #2b2d2e;
    --cover-skin: #b8aba0;
    --band: rgba(20,20,20,0.72);
  }
  * { box-sizing: border-box; margin: 0; padding: 0; }
  html, body { width: 1200px; height: 1008px; overflow: hidden; }
  body { background: var(--page-bg); position: relative; font-family: "EB Garamond", Georgia, serif; color: var(--text-light); }

  .ad { position: absolute; overflow: hidden; box-shadow: 2px 3px 6px rgba(0,0,0,0.35); }
  .ad-backdrop {
    position: absolute; inset: 0;
    background:
      radial-gradient(ellipse at 70% 35%, rgba(140,150,152,0.55), transparent 55%),
      radial-gradient(ellipse at 20% 60%, rgba(30,30,30,0.6), transparent 60%),
      linear-gradient(180deg, var(--panel-light) 0%, var(--panel-mid) 45%, var(--panel-dark) 100%);
  }
  .ad-square { left: 61px; top: 61px; width: 534px; height: 534px; }
  .ad-landscape { left: 61px; top: 647px; width: 534px; height: 300px; }
  .ad-portrait { left: 643px; top: 61px; width: 499px; height: 886px; }

  .headline, .price, .blurb {
    position: absolute; left: 0; right: 0; text-align: center;
    text-transform: uppercase; font-weight: 500; line-height: 1;
    text-shadow: 0 1px 4px var(--text-shadow), 0 0 10px rgba(0,0,0,0.4);
  }
  .keep-case { text-transform: none; }
  .quote-mark { font-style: italic; opacity: 0.85; font-size: 1.5em; line-height: 0; }

  .ad-square .headline { top: 27px; font-size: 23px; }
  .ad-square .price { top: 59px; font-size: 16px; }
  .ad-square .blurb { top: 469px; font-size: 10.4px; line-height: 12.5px; padding: 0 20px; }

  .ad-landscape .headline { top: 37px; left: 20px; right: 240px; font-size: 21px; }
  .ad-landscape .price { top: 72px; left: 20px; right: 240px; font-size: 15.5px; line-height: 19px; }
  .ad-landscape .blurb { top: 137px; left: 30px; right: 240px; font-size: 12.6px; line-height: 15.3px; }

  .ad-portrait .headline { top: 43px; font-size: 37px; }
  .ad-portrait .price { top: 646px; font-size: 26px; line-height: 32px; }
  .ad-portrait .blurb { top: 751px; font-size: 15px; line-height: 18.2px; padding: 0 30px; }

  .cover { position: absolute; overflow: hidden; box-shadow: 0 4px 18px rgba(0,0,0,0.55); font-size: var(--cs); }
  .cover-art {
    position: absolute; inset: 0;
    background:
      radial-gradient(ellipse 30% 55% at 50% 55%, var(--cover-skin), transparent 70%),
      radial-gradient(ellipse 45% 70% at 50% 60%, var(--cover-shade), transparent 75%),
      linear-gradient(90deg, #3d4243 0%, var(--cover-forest) 22%, #c9d0cf 50%, var(--cover-forest) 78%, #3a3f40 100%);
  }
  .cover-author {
    position: absolute; top: 0.5em; left: 0; right: 0; text-align: center;
    font-family: "Open Sans", Arial, sans-serif; font-size: 0.95em; letter-spacing: 0.04em;
    text-transform: uppercase; color: rgba(255,255,255,0.85);
  }
  .cover-title {
    position: absolute; top: 12.5em; left: 0; right: 0; text-align: center;
    font-family: "Cinzel", Georgia, serif; color: #f2f2f2; line-height: 1;
    text-shadow: 0 0 6px rgba(0,0,0,0.7);
  }
  .cover-title .lead { display: block; font-size: 1.5em; letter-spacing: 0.3em; }
  .cover-title .main { display: block; font-size: 2.9em; font-weight: 600; margin-top: 0.05em; }
  .cover-title .tagline { display: block; font-family: "EB Garamond", Georgia, serif; font-style: italic; font-size: 1.4em; margin-top: 0.3em; }
  .cover-genre {
    position: absolute; left: 0; right: 0; bottom: 0.8em; height: 2.2em; line-height: 2.2em;
    background: var(--band); text-align: center;
    font-family: "Open Sans", Arial, sans-serif; font-weight: 700; font-size: 0.9em; color: #fff;
  }
  .ad-square .cover { left: 163px; top: 103px; width: 209px; height: 333px; --cs: 10.4px; }
  .ad-landscape .cover { left: 348px; top: 24px; width: 158px; height: 251px; --cs: 7.9px; }
  .ad-portrait .cover { left: 89px; top: 107px; width: 322px; height: 511px; --cs: 16px; }
</style>
</head>
<body>

<section class="ad ad-square">
  <div class="ad-backdrop" role="img" aria-label="Unscharfer, dunkelgrauer Waldhintergrund"></div>
  <h2 class="headline">Jetzt im Handel</h2>
  <p class="price">Zum Einführungspreis von 0,99 €</p>
  <div class="cover">
    <div class="cover-art" role="img" aria-label="Buchcover-Illustration: Fantasy-Kriegerin in einem nebligen Wald"></div>
    <p class="cover-author">Konrad P. Waltershofen</p>
    <p class="cover-title"><span class="lead">Nächte in</span><span class="main">Veloria</span><span class="tagline">Erste Runde</span></p>
    <p class="cover-genre">Fantasy, Erotik</p>
  </div>
  <p class="blurb"><span class="quote-mark">„</span>Eines Tages kauft der Student Kilian ein neuartiges Online-Computerspiel<br>und wei<span class="keep-case">ß</span> zu diesem Zeitpunkt noch nicht, dass sich sein Sex-Leben<br>dadurch drastisch verbessern wird.<span class="quote-mark">“</span></p>
</section>

<section class="ad ad-landscape">
  <div class="ad-backdrop" role="img" aria-label="Unscharfer, dunkelgrauer Waldhintergrund"></div>
  <h2 class="headline">Jetzt im Handel</h2>
  <p class="price">Zum Einführungspreis<br>von 0,99 €</p>
  <p class="blurb"><span class="quote-mark">„</span>Eines Tages kauft der Student<br>Kilian ein neuartiges Online-<br>Computerspiel und wei<span class="keep-case">ß</span><br>zu diesem Zeitpunkt noch nicht,<br>dass sich sein Sex-Leben<br>dadurch drastisch<br>verbessern wird.<span class="quote-mark">“</span></p>
  <div class="cover">
    <div class="cover-art" role="img" aria-label="Buchcover-Illustration: Fantasy-Kriegerin in einem nebligen Wald"></div>
    <p class="cover-author">Konrad P. Waltershofen</p>
    <p class="cover-title"><span class="lead">Nächte in</span><span class="main">Veloria</span><span class="tagline">Erste Runde</span></p>
    <p class="cover-genre">Fantasy, Erotik</p>
  </div>
</section>

<section class="ad ad-portrait">
  <div class="ad-backdrop" role="img" aria-label="Unscharfer, dunkelgrauer Waldhintergrund"></div>
  <h2 class="headline">Jetzt im Handel</h2>
  <div class="cover">
    <div class="cover-art" role="img" aria-label="Buchcover-Illustration: Fantasy-Kriegerin in einem nebligen Wald"></div>
    <p class="cover-author">Konrad P. Waltershofen</p>
    <p class="cover-title"><span class="lead">Nächte in</span><span class="main">Veloria</span><span class="tagline">Erste Runde</span></p>
    <p class="cover-genre">Fantasy, Erotik</p>
  </div>
  <p class="price">Zum Einführungspreis<br>von 0,99 €</p>
  <p class="blurb"><span class="quote-mark">„</span>Eines Tages kauft der Student Kilian ein<br>neuartiges Online-Computerspiel<br>und wei<span class="keep-case">ß</span> zu diesem Zeitpunkt noch nicht,<br>dass sich sein Sex-Leben<br>dadurch drastisch verbessern wird.<span class="quote-mark">“</span></p>
</section>

</body>
</html>
```